DJ company new brochure of services offered

I would like to get a new price sheet made for my company services. Currently it's text only. I would like to add pictures next to each service description also like to add general background colors, and just make it look more attractive overall.

Uplighting - File #4 & file #10
Centerpiece pin-spots - File #15
Wedding Cake Spot - file #13 (can you crop out the logo at the bottom)?
Dance Floor Decal File #5
Gobo Monogram - File # 3
market lighting - file #14
ballroom draping - file #7
Video/projections screens: File #13
Indoor safe sparkler effect (not listed on price sheet yet) File #11
Dancing on a cloud - File #9
Co2 Cannons - File #6

Target Market(s)

bride and grooms

Industry/Entity Type

Entertainment

Font styles to use
Serif

Colors

Designer to choose colors to be used in the design.

Requirements
Must have
• my website is www.brightloomevents.example
• instagram is: @brightloomevents.example

```html
<!DOCTYPE html>
<html lang="en">
<head>
<meta charset="UTF-8">
<title>Additional Service Add-ons</title>
<link href="https://fonts.googleapis.com/css2?family=Crimson+Pro:wght@400;600&display=swap" rel="stylesheet">
<style>
  :root {
    --band: #5e5d66;
    --paper: #ffffff;
    --panel: #2a2a2c;
    --strip: #3d3d40;
    --list: #3a3a3d;
    --ink-light: #ffffff;
    --ink-soft: #e4e2ea;
    --ink-dark: #111111;
  }
  * { margin: 0; padding: 0; box-sizing: border-box; }
  html, body { width: 848px; height: 1200px; overflow: hidden; background: var(--panel); }
  body { font-family: "Crimson Pro", Georgia, serif; color: var(--ink-light); }
  .sheet { position: relative; width: 848px; height: 1200px; background: var(--panel); }
  .top-band { position: absolute; left: 0; top: 0; width: 848px; height: 48px; background: var(--band);
    display: flex; justify-content: space-between; align-items: center; padding: 0 28px;
    font-size: 19px; color: var(--ink-soft); letter-spacing: 0.02em; }
  .heading-bar { position: absolute; left: 0; top: 48px; width: 848px; height: 40px; background: var(--paper);
    color: var(--ink-dark); font-size: 26px; padding-left: 28px; line-height: 40px; }
  .strip { position: absolute; left: 0; width: 848px; height: 49px; background: var(--strip); }
  .title { position: absolute; font-size: 26px; font-weight: 600; line-height: 1; }
  .title span { font-weight: 400; }
  .item, .price { position: absolute; font-size: 22px; line-height: 1; }
  .price { font-size: 20px; }
  .stack { line-height: 22px; }
  .photos { position: absolute; left: 0; top: 88px; }
  .extras { position: absolute; left: 0; top: 1046px; width: 848px; height: 120px; background: var(--list); }
  .extras .name { position: absolute; left: 34px; font-size: 24px; font-weight: 600; line-height: 1; }
  .extras .name span { font-weight: 400; }
  .extras .cost { position: absolute; left: 458px; font-size: 20px; line-height: 1; }
  .footer { position: absolute; left: 0; top: 1166px; width: 848px; height: 34px; background: var(--band);
    font-size: 19px; padding-left: 32px; line-height: 34px; }
  .centered { text-align: center; width: 200px; left: 98px; }
</style>
</head>
<body>
<div class="sheet">
  <div class="top-band">
    <span class="website">www.brightloomevents.example</span>
    <span class="instagram">Instagram: @brightloomevents.example</span>
  </div>
  <div class="heading-bar">Additional Service Add-on : (when booked with DJ package)</div>

  <div class="strip" style="top:88px"></div>
  <div class="strip" style="top:328px"></div>
  <div class="strip" style="top:566px"></div>
  <div class="strip" style="top:806px"></div>

  <svg class="photos" width="848" height="958" viewBox="0 0 848 958">
    <defs>
      <clipPath id="photo-column"><path d="M436 0 Q614 470 432 958 L848 958 L848 0 Z"/></clipPath>
      <linearGradient id="tone-warm" x1="0" y1="0" x2="0" y2="1">
        <stop offset="0" stop-color="#8a6a5c"/><stop offset="0.5" stop-color="#c79a86"/><stop offset="1" stop-color="#3a2c2a"/>
      </linearGradient>
      <linearGradient id="tone-lavender" x1="0" y1="0" x2="0" y2="1">
        <stop offset="0" stop-color="#d6c7e8"/><stop offset="0.5" stop-color="#a88bc9"/><stop offset="1" stop-color="#7d6a99"/>
      </linearGradient>
      <linearGradient id="tone-violet" x1="0" y1="0" x2="0" y2="1">
        <stop offset="0" stop-color="#6b4f80"/><stop offset="0.5" stop-color="#c79adf"/><stop offset="1" stop-color="#e8d2f0"/>
      </linearGradient>
      <linearGradient id="tone-ballroom" x1="0" y1="0" x2="0" y2="1">
        <stop offset="0" stop-color="#4a3528"/><stop offset="0.5" stop-color="#a38266"/><stop offset="1" stop-color="#d8cbbd"/>
      </linearGradient>
    </defs>
    <g clip-path="url(#photo-column)">
      <rect role="img" aria-label="Banquet room washed in warm up-lighting with round dinner tables" x="0" y="0" width="848" height="240" fill="url(#tone-warm)"/>
      <rect role="img" aria-label="Draped reception hall with pin-spot lit floral centerpieces" x="0" y="240" width="848" height="238" fill="url(#tone-lavender)"/>
      <rect role="img" aria-label="Sweetheart table with a monogram projected onto the dance floor" x="0" y="478" width="848" height="240" fill="url(#tone-violet)"/>
      <rect role="img" aria-label="Couple dancing on a white dance floor with a name decal" x="0" y="718" width="848" height="240" fill="url(#tone-ballroom)"/>
    </g>
  </svg>

  <div class="title" style="left:27px;top:99px">Room up-lighting <span>(color of your choice).</span></div>
  <div class="item" style="left:26px;top:178px">20 fixtures (med-large room)</div>
  <div class="price" style="left:391px;top:183px">$400</div>
  <div class="item" style="left:26px;top:217px">16 fixtures (med-large room)</div>
  <div class="price" style="left:391px;top:218px">$350</div>
  <div class="item" style="left:26px;top:251px">12 fixtures (small-med room)</div>
  <div class="price" style="left:391px;top:254px">$300</div>

  <div class="title" style="left:30px;top:339px">Pin spot lighting</div>
  <div class="item stack" style="left:29px;top:433px">Wedding cake<br>Centerpieces<br>Sweetheart table / etc.</div>
  <div class="price" style="left:392px;top:454px">$30+</div>

  <div class="title" style="left:32px;top:578px">Dance Floor Decal / Gobo Monogram</div>
  <div class="item stack" style="left:31px;top:683px">B&amp;G names appear<br>onto wall or dance floor</div>
  <div class="price" style="left:391px;top:694px">$250+</div>

  <div class="title" style="left:30px;top:818px">White Dance Floor <span>(Square or Round)</span></div>
  <div class="item stack centered" style="top:928px">$1000+<br>(seamless only)</div>

  <div class="extras">
    <div class="name" style="top:5px">Dance floor lighting</div>
    <div class="cost" style="top:7px">$200+ (depending on style)</div>
    <div class="name" style="top:33px">A/V <span>(screens, projectors, video display)</span></div>
    <div class="cost" style="top:35px">$200+</div>
    <div class="name" style="top:61px">String/Bistro Lighting</div>
    <div class="cost" style="top:63px">Depends on size – contact us</div>
    <div class="name" style="top:89px">Indoor Sparklers / CO2 Cannons</div>
    <div class="cost" style="top:91px">Contact us for pricing</div>
  </div>

  <div class="footer">*We offer a wide range of additional services. Please contact us for more info &amp; pricing.</div>
</div>
</body>
</html>
```